Property Management Company Business Cards

Need business cards for a property management company located in Michigan. We manage houses for clients all over the world. Young and modern company, looking for eye catching design. Please work with the attached logo.

Industry/Entity Type

Property Management

Requirements
Must have
• Need lines for address, telephone number, fax number, web site.

Also lines for name, and job title

```html
<!DOCTYPE html>
<html lang="en">
<head>
<meta charset="utf-8">
<title>Lakeshore Harbor Management – Business Cards</title>
<link rel="stylesheet" href="https://fonts.googleapis.com/css2?family=Open+Sans:wght@400;600;700&display=swap">
<style>
  :root {
    --page-bg: #e9e6e2;
    --card-white: #ffffff;
    --card-black: #0b0b0b;
    --brand-blue: #3d86c2;
    --swoosh-dark: #343437;
    --ink: #141414;
    --ink-soft: #2a2a2a;
    --back-shade: #1b1b1b;
  }
  * { box-sizing: border-box; margin: 0; padding: 0; }
  html, body {
    width: 1200px; height: 900px; overflow: hidden;
    background: var(--page-bg);
    font-family: "Open Sans", Arial, sans-serif;
  }
  .canvas {
    position: relative; width: 1200px; height: 900px;
  }
  .card {
    position: absolute; top: 302px;
    width: 520px; height: 297px;
    border-radius: 18px; overflow: hidden;
    box-shadow: 0 10px 24px rgba(0,0,0,0.25);
  }
  .card--front { left: 60px; background: var(--card-white); }
  .card--back { left: 620px; background: var(--card-black); }
  .card__waves { position: absolute; inset: 0; }

  .brand {
    position: absolute; display: flex; align-items: center; gap: 10px;
  }
  .brand__dot {
    width: 30px; height: 30px; border-radius: 50%;
    background: var(--brand-blue); flex: none;
  }
  .brand__name {
    font-weight: 700; color: var(--ink-soft);
    font-size: 20px; line-height: 1.05; letter-spacing: 0.5px;
    text-transform: uppercase;
  }
  .card--front .brand { left: 28px; top: 28px; }

  .person {
    position: absolute; left: 0; width: 330px; top: 122px; text-align: center;
  }
  .person__name { font-weight: 700; font-size: 19px; color: var(--ink); }
  .person__title { font-size: 15px; color: var(--ink); margin-top: 4px; }

  .contact {
    position: absolute; right: 24px; top: 200px; text-align: right;
    font-weight: 600; font-size: 13.5px; line-height: 1.3; color: var(--ink);
  }
  .contact__phones { margin-top: 8px; }

  .website {
    position: absolute; left: 26px; bottom: 24px;
    font-weight: 700; font-size: 15px; color: var(--ink);
  }

  .back__mark {
    position: absolute; left: 145px; top: 30px;
    width: 240px; height: 240px; border-radius: 50%;
    background: var(--back-shade);
  }
  .card--back .brand {
    left: 50%; top: 50%; transform: translate(-50%, -50%); gap: 7px;
  }
  .card--back .brand__dot { width: 18px; height: 18px; }
  .card--back .brand__name { color: #ffffff; font-size: 11px; }
</style>
</head>
<body>
<main class="canvas">
  <section class="card card--front" aria-label="Business card front">
    <svg class="card__waves" viewBox="0 0 520 297" preserveAspectRatio="none" aria-hidden="true">
      <path d="M0,224 C170,216 380,150 520,16 L520,297 L0,297 Z" fill="var(--swoosh-dark)"/>
      <path d="M0,233 C170,228 390,176 520,52 L520,297 L0,297 Z" fill="var(--brand-blue)"/>
    </svg>
    <div class="brand">
      <span class="brand__dot"></span>
      <span class="brand__name">Lakeshore Harbor<br>Management</span>
    </div>
    <div class="person">
      <p class="person__name">Firstname Lastname</p>
      <p class="person__title">property manager</p>
    </div>
    <address class="contact">
      <p>4120 Maple Row</p>
      <p>Brightford, MI 48000</p>
      <div class="contact__phones">
        <p>Tel. 555-210-4612</p>
        <p>Fax 555-210-4615</p>
      </div>
    </address>
    <p class="website">www.lakeshoreharbor.com</p>
  </section>

  <section class="card card--back" aria-label="Business card back">
    <div class="back__mark"></div>
    <div class="brand">
      <span class="brand__dot"></span>
      <span class="brand__name">Lakeshore Harbor<br>Management</span>
    </div>
  </section>
</main>
</body>
</html>
```